Real Estate Marketing Postcards need a fresh look, Front & Back

I have a current postcard design (attached) that lacks design quality and too much use of color. I do like the basic color scheme, but I'm open to anything that cleans up the look and incorporates space for the existing text. I'm not opposed to a design with a white background, more white space. The design should be full bleed according to the attached specs. I would like this to be sent over in an Adobe format, something like InDesign.

The company logo will remain the same colors and appearance. The headshot will likely be updated in the coming weeks.

I am attaching a sample of a recent card plus a template from the printer showing the back of the card and location of the address and postage section that must remain blank. I am also including the logo and another logo designed for use with a white (or non blue) background.

(feel free to swap in stock photos of whatever house you want, but the front of the card should incorporate at least one photo of a house.)

Target Market(s)

Home owners.

Industry/Entity Type

Real Estate

Font styles to use
Sans Serif

Colors

Designer to choose colors to be used in the design.

Requirements
Must have
• Company logo, the headshot, the contact info on the back, a photo or photos of a house along with the text "Just Sold" or "Sold" featured on the front of the card.

```html
<!DOCTYPE html>
<html lang="en">
<head>
<meta charset="utf-8">
<title>Postcard – Front &amp; Back</title>
<link rel="stylesheet" href="https://fonts.googleapis.com/css2?family=Oswald:wght@500;600&family=Open+Sans:wght@600;700;800&family=Tinos&display=swap">
<style>
  :root {
    --navy: #1b4f8c;
    --navy-deep: #164478;
    --sky: #5bb4e5;
    --pale: #a9d6f2;
    --ink: #2b2b2b;
    --rule: #b9b9b9;
    --page: #ececec;
    --white: #ffffff;
  }
  * { box-sizing: border-box; margin: 0; padding: 0; }
  html, body { width: 800px; height: 1200px; overflow: hidden; }
  body { background: var(--page); position: relative; font-family: "Open Sans", sans-serif; }

  .card { position: absolute; left: 40px; width: 720px; height: 504px; overflow: hidden; box-shadow: 0 6px 14px rgba(0,0,0,.25); background: var(--white); }
  .card--front { top: 64px; }
  .card--back { top: 632px; }

  /* Front */
  .house-photo { position: absolute; left: 0; top: 0; width: 720px; height: 390px;
    background: linear-gradient(180deg, #cfdbe6 0%, #9eb0c4 25%, #4d5f86 50%, #5f7d4a 72%, #5f9a3a 100%); }
  .headline-sold { position: absolute; right: 24px; top: 6px; font-family: "Oswald", sans-serif; font-weight: 600; font-size: 46px; color: var(--white); letter-spacing: 1px; text-shadow: 0 1px 3px rgba(0,0,0,.35); }
  .front-band { position: absolute; left: 0; top: 382px; width: 720px; height: 122px; background: var(--navy); border-top: 8px solid var(--sky); }
  .brand { position: absolute; left: 10px; top: 20px; display: flex; align-items: center; gap: 6px; }
  .brand__mark { width: 14px; height: 14px; background: var(--sky); }
  .brand__name { font-weight: 700; font-size: 17px; color: var(--white); line-height: 1.05; }
  .front-phone { position: absolute; left: 12px; top: 78px; font-size: 17px; color: var(--white); font-weight: 600; }
  .listed-by { position: absolute; left: 160px; width: 390px; top: 14px; text-align: center; color: var(--white); }
  .listed-by__lead { font-weight: 800; font-size: 23px; letter-spacing: .5px; }
  .listed-by__agent { font-family: "Tinos", serif; font-size: 21px; letter-spacing: 1px; margin-top: 2px; }
  .listed-by__tag { font-weight: 700; font-size: 13px; margin-top: 10px; }
  .front-headshot { position: absolute; left: 570px; top: 353px; width: 150px; height: 151px; background: linear-gradient(180deg, #2a64a6, #1b4f8c); border-left: 4px solid var(--navy); }

  /* Back */
  .back-deco { position: absolute; left: 0; top: 0; }
  .tagline { position: absolute; left: 210px; top: 51px; height: 40px; line-height: 40px; font-family: "Oswald", sans-serif; font-weight: 500; font-size: 11.5px; color: var(--white); }
  .postage { position: absolute; left: 588px; top: 18px; width: 98px; height: 100px; background: var(--white); border: 1px solid #d5d5d5; }
  .pitch { position: absolute; left: 5px; top: 142px; width: 340px; font-family: "Tinos", serif; color: var(--ink); font-size: 12.5px; line-height: 1.3; }
  .pitch__title { font-family: "Open Sans", sans-serif; font-weight: 800; font-size: 24px; color: var(--navy); margin-left: 66px; letter-spacing: .5px; }
  .pitch__sub { font-family: "Open Sans", sans-serif; font-weight: 600; font-size: 12.5px; color: var(--sky); margin-left: 10px; }
  .pitch p + p { margin-top: 6px; }
  .pitch__gap { margin-top: 22px !important; }
  .address-lines { position: absolute; left: 412px; top: 235px; width: 276px; }
  .address-lines span { display: block; height: 1px; background: var(--rule); margin-bottom: 58px; }
  .back-headshot { position: absolute; left: 7px; top: 353px; width: 144px; height: 146px; background: linear-gradient(180deg, #e2e2e2, #c9c9c9); }
  .agent { position: absolute; left: 159px; top: 364px; }
  .agent__name { font-weight: 700; font-size: 16px; color: var(--navy); }
  .agent__title { font-weight: 600; font-size: 12px; color: var(--sky); }
  .agent__role { font-family: "Tinos", serif; font-size: 11.5px; color: var(--ink); }
  .contact-box { position: absolute; left: 357px; top: 426px; width: 363px; height: 78px; background: var(--navy); color: var(--white); font-family: "Tinos", serif; text-align: center; padding-top: 6px; }
  .contact-box__firm { font-family: "Open Sans", sans-serif; font-weight: 600; font-size: 11px; letter-spacing: .3px; }
  .contact-box__phones { display: flex; justify-content: space-between; font-size: 11px; padding: 2px 28px 0 36px; }
  .contact-box__web { font-size: 11px; }
  .contact-box__note { font-size: 6.5px; margin-top: 4px; opacity: .9; }
</style>
</head>
<body>

<section class="card card--front">
  <div class="house-photo" role="img" aria-label="Photo of a blue craftsman-style house with white porch columns, stone base and green lawn"></div>
  <div class="headline-sold">JUST SOLD</div>
  <div class="front-band">
    <div class="brand"><span class="brand__mark"></span><span class="brand__name">Maple Ridge<br>Real Estate</span></div>
    <div class="front-phone">(555) 240-1180</div>
    <div class="listed-by">
      <div class="listed-by__lead">ANOTHER HOME JUST LISTED BY</div>
      <div class="listed-by__agent">THE HOLLOWELL REALTOR</div>
      <div class="listed-by__tag">You KNOW it wont last long!</div>
    </div>
  </div>
  <div class="front-headshot" role="img" aria-label="Agent headshot"></div>
</section>

<section class="card card--back">
  <svg class="back-deco" width="720" height="130" viewBox="0 0 720 130" aria-hidden="true">
    <rect x="140" y="51" width="580" height="40" fill="var(--navy)"/>
    <polygon points="20,0 270,0 150,116 132,70" fill="var(--navy)"/>
    <polygon points="0,0 42,0 42,40 0,40" fill="var(--pale)"/>
    <polygon points="38,28 70,8 84,58 52,78" fill="var(--sky)"/>
    <polygon points="22,70 48,54 56,90 30,104" fill="var(--pale)"/>
    <polygon points="60,66 92,50 100,96 68,110" fill="var(--pale)"/>
    <polygon points="148,70 176,50 176,94 156,118" fill="var(--pale)"/>
  </svg>
  <div class="tagline">THE RIGHT AGENT WILL GET YOU HOME SELL FASTER. TRY HOLLOWELL REALTOR</div>
  <div class="postage"></div>

  <div class="pitch">
    <div class="pitch__title">SELLING?</div>
    <div class="pitch__sub">YOUR HOME IS YOUR BIGGEST ASSET.</div>
    <p>Choosing the right agent is critical to your success.</p>
    <p class="pitch__gap">Choosing the local agent with the experise to position your Hollowell home and get it sold fast and for top dollar.</p>
    <p>There is no other agent who knows the Hollowell market better. Contact me today to get your home SOLD.</p>
  </div>

  <div class="address-lines"><span></span><span></span><span></span></div>

  <div class="back-headshot" role="img" aria-label="Agent headshot"></div>
  <div class="agent">
    <div class="agent__name">DARIO CASTELLANO</div>
    <div class="agent__title">THE HOLLOWELL REALTOR</div>
    <div class="agent__role">Principal Broker, REALTOR</div>
  </div>

  <div class="contact-box">
    <div class="contact-box__firm">MAPLE RIDGE REAL ESTATE</div>
    <div class="contact-box__phones"><span>office: (555) 240-1180</span><span>Cell: (555) 318-4472</span></div>
    <div class="contact-box__web">www.hollowellhomes.com</div>
    <div class="contact-box__note">If your home is currently listed with another broker, this is not intended as a solicitation of that listing.</div>
  </div>
</section>

</body>
</html>
```